Relocation/furniture installation company needs new business cards

we are a relocation and furniture installation company mainly dealing with corporate clients and we are looking for new business card ideas. Cards should incorporate our logo and list our website, phone number and services. The company is only 2 years old but with more staff joining we are in the need for more business cards, so something with an awesome design that is eye catching would go a long way to insure we get our name out there and look good to potential new clients.

Target Market(s)

Corporate

Industry/Entity Type

Trade

Contact Information for Business Card

www.mervoline.co.nz
0508 4 bravok

furniture installation
business relocations
joinery installation
commercial property maintenance

Colors
0592cd
34a7d8
85cae6
85acd3
0356a4
cfdfed
cee9f5
757575
474747

Requirements
Must have
• Business relocations and furniture installation specialists
Nice to have
• something that incorporates our logo.

```html
<!DOCTYPE html>
<html lang="en">
<head>
<meta charset="utf-8">
<title>Mervoline Business Card</title>
<link rel="stylesheet" href="https://fonts.googleapis.com/css2?family=Lato:wght@400;700&family=Montserrat:wght@400;600;700&display=swap">
<style>
  :root {
    --blue-deep: #0356a4;
    --blue-main: #0d55a8;
    --blue-bright: #0592cd;
    --blue-sky: #34a7d8;
    --blue-pale: #85cae6;
    --blue-soft: #cee9f5;
    --blue-mist: #e3f0f8;
    --navy-band: #22389a;
    --grey-mid: #757575;
    --white: #ffffff;
    --stage: #dfe7ee;
  }
  * { box-sizing: border-box; margin: 0; padding: 0; }
  html, body { width: 1200px; height: 1200px; overflow: hidden; }
  body {
    background: var(--stage);
    font-family: "Lato", sans-serif;
    display: flex; flex-direction: column; align-items: center;
    justify-content: center; gap: 52px;
  }
  .card {
    position: relative; width: 900px; height: 514px; overflow: hidden;
    box-shadow: 0 8px 24px rgba(3, 40, 90, .18);
  }

  /* ---------- Back of card ---------- */
  .card-back { background: var(--blue-main); }
  .services-panel {
    position: absolute; left: 0; top: 0; width: 520px; height: 100%;
    background: var(--blue-main); padding-top: 92px;
  }
  .services-heading {
    background: var(--blue-pale); width: 430px; height: 52px;
    display: flex; align-items: center; padding-left: 58px;
    font-family: "Montserrat", sans-serif; font-size: 34px; color: var(--blue-deep);
    letter-spacing: .5px;
  }
  .services-heading strong { font-weight: 700; margin-right: 8px; }
  .services-heading span { font-weight: 400; color: var(--blue-main); }
  .services-list { list-style: none; margin: 34px 0 0 62px; }
  .services-list li {
    display: flex; align-items: flex-start; gap: 14px;
    font-family: "Montserrat", sans-serif; font-size: 25px; line-height: 1.05;
    color: var(--white); margin-bottom: 22px;
  }
  .services-list svg { flex: none; margin-top: 4px; }
  .photo-area {
    position: absolute; right: 0; top: 0; width: 440px; height: 100%;
    background: linear-gradient(160deg, #c9d6de 0%, #8ea3b2 45%, #b96a3a 100%);
  }
  .brand-seal {
    position: absolute; left: 390px; top: 120px; width: 250px; height: 250px;
    border-radius: 50%; background: var(--white);
    border: 10px solid var(--blue-deep);
    box-shadow: 0 0 0 6px var(--white);
    display: flex; align-items: center; justify-content: center;
  }
  .brand-name {
    font-family: "Montserrat", sans-serif; font-weight: 700;
    color: var(--blue-deep); letter-spacing: 2px;
  }
  .brand-seal .brand-name { font-size: 28px; }

  /* ---------- Front of card ---------- */
  .card-front { background: var(--blue-mist); }
  .skyline {
    position: absolute; left: 0; top: 40px; width: 100%; height: 300px;
    background: linear-gradient(180deg, rgba(200,212,222,0) 0%, rgba(200,212,222,.7) 100%);
  }
  .front-shape { position: absolute; inset: 0; }
  .front-brand {
    position: absolute; left: 330px; top: 118px;
    display: flex; align-items: center; gap: 14px;
  }
  .front-brand .brand-mark {
    width: 22px; height: 22px; border-radius: 50%; background: var(--blue-deep);
  }
  .front-brand .brand-name { font-size: 52px; }
  .name-band {
    position: absolute; left: 360px; top: 212px;
    background: var(--navy-band); padding: 8px 22px;
    font-family: "Lato", sans-serif; font-size: 46px; color: var(--white);
    letter-spacing: .5px;
  }
  .name-band strong { font-weight: 700; }
  .name-band span { font-weight: 400; color: var(--blue-pale); }
  .job-title {
    position: absolute; left: 382px; top: 290px;
    font-size: 22px; color: var(--white); letter-spacing: .5px;
  }
  .contact-row {
    position: absolute; left: 60px; right: 40px; bottom: 44px;
    display: flex; justify-content: space-between; align-items: center;
  }
  .contact-item { display: flex; align-items: center; gap: 14px; }
  .contact-icon {
    width: 40px; height: 40px; border: 2px solid var(--blue-pale); border-radius: 8px;
    display: flex; align-items: center; justify-content: center; flex: none;
  }
  .contact-text { font-size: 20px; line-height: 1.2; color: var(--white); }
</style>
</head>
<body>

  <!-- Back -->
  <section class="card card-back">
    <div class="services-panel">
      <h2 class="services-heading"><strong>OUR</strong><span>SERVICES</span></h2>
      <ul class="services-list">
        <li><svg width="22" height="22" viewBox="0 0 22 22"><circle cx="11" cy="11" r="9" fill="none" stroke="#85cae6" stroke-width="2"/><path d="M6 11l4 4 7-8" fill="none" stroke="#85cae6" stroke-width="2.2"/></svg>Furniture<br>Installation</li>
        <li><svg width="22" height="22" viewBox="0 0 22 22"><circle cx="11" cy="11" r="9" fill="none" stroke="#85cae6" stroke-width="2"/><path d="M6 11l4 4 7-8" fill="none" stroke="#85cae6" stroke-width="2.2"/></svg>Business<br>Relocations</li>
        <li><svg width="22" height="22" viewBox="0 0 22 22"><circle cx="11" cy="11" r="9" fill="none" stroke="#85cae6" stroke-width="2"/><path d="M6 11l4 4 7-8" fill="none" stroke="#85cae6" stroke-width="2.2"/></svg>Joinery<br>Installation</li>
        <li><svg width="22" height="22" viewBox="0 0 22 22"><circle cx="11" cy="11" r="9" fill="none" stroke="#85cae6" stroke-width="2"/><path d="M6 11l4 4 7-8" fill="none" stroke="#85cae6" stroke-width="2.2"/></svg>Commercial Property<br>Maintenance</li>
      </ul>
    </div>
    <div class="photo-area" role="img" aria-label="Photo of two installers fitting an office desk in a bright workspace"></div>
    <div class="brand-seal"><span class="brand-name">MERVOLINE</span></div>
  </section>

  <!-- Front -->
  <section class="card card-front">
    <div class="skyline" role="img" aria-label="Faint city skyline silhouette"></div>
    <svg class="front-shape" viewBox="0 0 900 514" preserveAspectRatio="none">
      <path d="M0 330 C 260 330, 620 260, 900 110 L900 514 L0 514 Z" fill="#34a7d8"/>
      <path d="M0 346 C 260 346, 630 278, 900 128 L900 514 L0 514 Z" fill="#0d55a8"/>
    </svg>
    <div class="front-brand"><span class="brand-mark"></span><span class="brand-name">MERVOLINE</span></div>
    <div class="name-band"><strong>LIAM</strong> <span>CARTER</span></div>
    <div class="job-title">MANAGING DIRECTOR</div>
    <div class="contact-row">
      <div class="contact-item">
        <span class="contact-icon"><svg width="22" height="22" viewBox="0 0 24 24"><path d="M6 3l4 4-2 3c1 3 3 5 6 6l3-2 4 4-3 3C10 21 3 14 3 6z" fill="none" stroke="#cee9f5" stroke-width="1.8"/></svg></span>
        <span class="contact-text">(012) 555-0147<br>0508 4 bravok</span>
      </div>
      <div class="contact-item">
        <span class="contact-icon"><svg width="22" height="22" viewBox="0 0 24 24"><circle cx="12" cy="12" r="9" fill="none" stroke="#cee9f5" stroke-width="1.8"/><path d="M3 12h18M12 3c4 4 4 14 0 18M12 3c-4 4-4 14 0 18" fill="none" stroke="#cee9f5" stroke-width="1.5"/></svg></span>
        <span class="contact-text">liam@mervoline.co.nz<br>www.mervoline.co.nz</span>
      </div>
      <div class="contact-item">
        <span class="contact-icon"><svg width="22" height="22" viewBox="0 0 24 24"><path d="M3 12l9-8 9 8M6 10v10h12V10" fill="none" stroke="#cee9f5" stroke-width="1.8"/></svg></span>
        <span class="contact-text">48 Harbour Lane,<br>Suite 7 Wellford, NZ 6011</span>
      </div>
    </div>
  </section>

</body>
</html>
```